Website for a Steadwell, an HVAC company.

We are a company that provides residential and commercial service. We don’t need any widgets other than a call to action where customers can message us. Though we have very few google reviews, they are all great and would like to see those populated. Simple and modern is the style. I included our logo and a pic of our vans.

Target Market(s)

Residential customers

Coding

Coded - Design and coding required

Number of Pages Required

1 page

Font styles to use
Sans Serif

Colors
0054AA
0677BA
7BADD7
CADEEF
E8F1F8
EE7325
F08F49
F5BC92
FAE3D3
FDF4ED

```html
<!DOCTYPE html>
<html lang="en">
<head>
<meta charset="utf-8">
<title>Steadwell Heating and Air</title>
<link href="https://fonts.googleapis.com/css2?family=Oswald:wght@400;500;600&family=Montserrat:wght@400;500;600;700&display=swap" rel="stylesheet">
<style>
:root{
  --blue-deep:#0054AA;
  --blue:#0677BA;
  --blue-mid:#7BADD7;
  --blue-pale:#CADEEF;
  --blue-wash:#E8F1F8;
  --orange:#EE7325;
  --orange-mid:#F08F49;
  --orange-soft:#F5BC92;
  --orange-pale:#FAE3D3;
  --cream:#FDF4ED;
  --ink:#111820;
  --text:#2b2f36;
  --footer:#0c1624;
  --btn-a:#2f9be0;
  --btn-b:#1f7fd0;
  --star:#00b67a;
}
*{box-sizing:border-box;margin:0;padding:0}
html,body{width:1200px;height:4959px;overflow:hidden}
body{position:relative;background:#fff;font-family:'Montserrat',sans-serif;color:var(--text)}
.abs{position:absolute}
.heading{font-family:'Oswald',sans-serif;font-weight:500;text-transform:uppercase;color:var(--ink);letter-spacing:.2px}
.btn{position:absolute;display:flex;align-items:center;justify-content:center;border-radius:22px;background:linear-gradient(90deg,var(--btn-a),var(--btn-b));color:#fff;font-size:11.5px;font-weight:700;text-transform:uppercase;letter-spacing:.3px;box-shadow:0 6px 14px rgba(6,119,186,.25)}
.ph{position:absolute}
/* hero */
.hero{position:absolute;left:0;top:0;width:1200px;height:718px;background:linear-gradient(120deg,#2b3036 0%,#1d2227 45%,#30363c 100%);overflow:hidden}
.hero-photo{left:0;top:0;width:1200px;height:718px;background:radial-gradient(circle at 40% 30%,rgba(60,70,80,.7),rgba(20,24,28,.2) 60%),linear-gradient(90deg,rgba(80,90,100,.35),rgba(20,24,28,.1))}
.topbar{position:absolute;top:0;left:760px;height:38px;display:flex}
.topbar .call{width:180px;background:var(--orange);clip-path:polygon(8% 0,100% 0,92% 100%,0 100%);color:#fff;font-size:12.5px;font-weight:600;display:flex;align-items:center;justify-content:center;gap:6px}
.topbar .social{width:190px;margin-left:-14px;background:var(--blue);clip-path:polygon(8% 0,100% 0,100% 100%,0 100%);display:flex;align-items:center;justify-content:center;gap:14px;padding-left:10px}
.dot-icon{width:12px;height:12px;border-radius:50%;border:1.5px solid #fff}
.brand{position:absolute;left:112px;top:128px;text-align:center;width:184px}
.brand .mark{width:14px;height:14px;border-radius:50%;background:var(--orange);margin:0 auto 8px}
.brand .name{font-family:'Montserrat',sans-serif;font-weight:700;font-size:18px;letter-spacing:3px;color:var(--blue)}
.brand .tag{font-size:8.5px;letter-spacing:3.5px;color:var(--blue);font-weight:600;margin-top:2px}
.nav{position:absolute;top:67px;left:414px;display:flex;align-items:center;gap:0}
.nav a{color:#fff;font-size:12.5px;font-weight:600;text-decoration:none;text-transform:uppercase;position:absolute;white-space:nowrap}
.hero-title{position:absolute;left:678px;top:222px;color:#fff;font-family:'Oswald',sans-serif;text-transform:uppercase}
.hero-title .l1{font-size:46px;line-height:56px;font-weight:400}
.hero-title .l2{font-size:150px;line-height:140px;font-weight:500;color:var(--orange);letter-spacing:2px;margin-top:-2px}
.hero-title .l3{font-size:46px;line-height:56px;font-weight:400;margin-top:-4px}
.hero-sub{position:absolute;left:683px;top:476px;width:400px;color:#fff;font-size:13px;line-height:19px}
/* enquiry */
.enquiry{position:absolute;left:0;top:718px;width:1200px;height:274px;background:var(--blue-wash)}
.field{position:absolute;background:#fff;border:1px solid #e1e7ee;border-radius:3px;font-size:8.5px;color:#9aa3ad;padding:8px 8px}
.van{left:676px;top:636px;width:524px;height:410px;border-radius:40px 20px 30px 30px;background:linear-gradient(160deg,#3b3f44 0%,#15181b 55%,#2c3035 100%)}
/* about */
.about-photo{left:676px;top:1050px;width:440px;height:550px;border-radius:50% 50% 50% 50%/40% 40% 60% 60%;background:linear-gradient(160deg,var(--blue-pale),var(--blue-mid) 40%,var(--blue-deep) 80%)}
.para{font-size:13.2px;line-height:19.6px;color:var(--text)}
/* services */
.services{position:absolute;left:0;top:1705px;width:1200px;height:502px;background:var(--blue-deep)}
.svc-card{position:absolute;top:165px;width:534px;height:272px;background:#fff;border-radius:4px}
.svc-img{position:absolute;left:12px;top:16px;width:172px;height:240px;border-radius:3px}
.svc-card h3{position:absolute;left:222px;top:48px;font-family:'Oswald',sans-serif;font-weight:500;font-size:17px;color:var(--ink);text-transform:uppercase}
.svc-card p{position:absolute;left:222px;top:80px;width:292px;font-size:13px;line-height:21px;color:var(--text)}
/* specialise */
.spec-item h4{font-family:'Oswald',sans-serif;font-weight:500;font-size:17px;text-transform:uppercase;color:var(--ink)}
.spec-item p{font-size:13px;line-height:19px;color:var(--text);margin-top:2px}
.spec-icon{position:absolute;width:70px;height:70px;border-radius:50%;background:#fff;border:1px solid #e4e8ee;box-shadow:0 4px 10px rgba(0,0,0,.05);display:flex;align-items:center;justify-content:center}
/* energy */
.energy{position:absolute;left:0;top:3028px;width:1200px;height:377px;background:var(--orange)}
.energy-photo{left:724px;top:3093px;width:352px;height:397px;border-radius:4px;background:linear-gradient(150deg,#e9ecef,#c9d3dd 45%,#3f6fa8 100%);box-shadow:0 18px 30px rgba(0,0,0,.18)}
/* reviews */
.review{position:absolute;top:3694px;width:322px;height:258px;background:#fff;box-shadow:0 4px 22px rgba(0,0,0,.09);border-radius:4px}
.review .stars{position:absolute;left:27px;top:27px;display:flex;gap:2px}
.review .stars span{width:19px;height:19px;background:var(--star);display:flex;align-items:center;justify-content:center}
.review .verified{position:absolute;left:140px;top:28px;font-size:12.5px;color:#555;display:flex;align-items:center;gap:5px}
.review .quote{position:absolute;right:30px;top:-22px}
.review p{position:absolute;left:27px;top:74px;width:270px;font-size:12.5px;line-height:19.5px;font-style:italic;color:#555}
.review .who{position:absolute;left:27px;font-family:'Oswald',sans-serif;font-size:16px;color:var(--ink)}
/* contact */
.contact{position:absolute;left:0;top:4131px;width:1200px;height:484px;background:var(--blue-deep)}
.contact-photo{left:115px;top:4141px;width:405px;height:474px;border-radius:50% 50% 6px 6px/35% 35% 6px 6px;background:linear-gradient(170deg,#2b6fc0,#0a3c82 60%,#d97a30 100%)}
.cfield{position:absolute;background:#fff;border-radius:3px;font-size:8.5px;color:#9aa3ad;padding:12px 26px}
/* footer */
.footer{position:absolute;left:0;top:4615px;width:1200px;height:344px;background:var(--footer);color:#fff}
.footer h5{position:absolute;font-family:'Oswald',sans-serif;font-weight:500;font-size:13px;padding-left:8px;border-left:2px solid var(--blue);line-height:14px}
.footer ul{list-style:none;position:absolute;font-size:9.5px;line-height:19px}
.fsoc{width:22px;height:22px;border-radius:50%;background:#fff;display:inline-block;margin-right:7px}
</style>
</head>
<body>

<!-- HERO -->
<header class="hero">
  <div class="ph hero-photo" role="img" aria-label="Photo of a technician servicing an HVAC unit"></div>
  <div class="topbar">
    <div class="call"><svg width="12" height="12" viewBox="0 0 24 24"><path fill="#fff" d="M6.6 10.8a15 15 0 0 0 6.6 6.6l2.2-2.2c.3-.3.7-.4 1-.2 1.1.4 2.3.6 3.6.6.6 0 1 .4 1 1V20c0 .6-.4 1-1 1A17 17 0 0 1 3 4c0-.6.4-1 1-1h3.5c.6 0 1 .4 1 1 0 1.3.2 2.5.6 3.6.1.3 0 .7-.2 1z"/></svg>555.014.2288</div>
    <div class="social"><span class="dot-icon"></span><span class="dot-icon"></span><span class="dot-icon"></span><span class="dot-icon"></span></div>
  </div>
  <div class="brand">
    <div class="mark"></div>
    <div class="name">STEADWELL</div>
    <div class="tag">HEATING AND AIR</div>
  </div>
  <nav class="nav">
    <svg class="abs" style="left:0;top:-1px" width="16" height="15" viewBox="0 0 24 22"><path fill="#EE7325" d="M12 1 1 11h3v10h6v-6h4v6h6V11h3z"/></svg>
    <a style="left:39px">About Us</a>
    <a style="left:148px">Services</a>
    <a style="left:251px">Testimonials</a>
    <a style="left:389px">Specials</a>
    <a style="left:491px">Contact Us</a>
  </nav>
  <h1 class="hero-title">
    <div class="l1">Keep your friends and</div>
    <div class="l2">Family</div>
    <div class="l3">Comfortable</div>
  </h1>
  <p class="hero-sub">We Now Offer a Full Line of Sanitation Services to Combat Covid-19! Ask Us About These Services Today!</p>
  <a class="btn" style="left:678px;top:533px;width:141px;height:42px">Contact Us</a>
</header>

<!-- ENQUIRY -->
<section class="enquiry">
  <h2 class="heading abs" style="left:152px;top:36px;font-size:36px;font-weight:400">Enquiry Form</h2>
  <p class="abs" style="left:153px;top:78px;font-size:13px">Get free quote now from our expert</p>
  <div class="field" style="left:154px;top:106px;width:129px;height:31px">Your Name</div>
  <div class="field" style="left:295px;top:106px;width:127px;height:31px">Phone</div>
  <div class="field" style="left:431px;top:106px;width:199px;height:72px">Your Message</div>
  <div class="field" style="left:154px;top:147px;width:129px;height:31px">Email</div>
  <div class="field" style="left:295px;top:147px;width:127px;height:31px">Contact Prefer Time</div>
  <a class="btn" style="left:154px;top:197px;width:158px;height:42px">Send Message</a>
</section>
<div class="ph van" role="img" aria-label="Photo of a black company service van"></div>

<!-- ABOUT -->
<section>
  <p class="abs" style="left:88px;top:1166px;font-size:14px;font-weight:500;color:var(--ink)">ABOUT US</p>
  <h2 class="heading abs" style="left:88px;top:1192px;font-size:38px;font-weight:400">Why Choose Us?</h2>
  <p class="para abs" style="left:88px;top:1244px;width:512px">At Steadwell Heating and Air, we believe in delivering high-quality HVAC solutions that ensure year-round comfort for your home or business. With years of experience, our certified technicians provide expert installation, maintenance, and repair services tailored to your needs. We take pride in our customer-first approach, offering transparent pricing, honest recommendations, and fast, reliable service. Whether you need a new heating system, air conditioning repair, or routine maintenance, we are committed to keeping your indoor environment comfortable and efficient."</p>
  <a class="btn" style="left:88px;top:1446px;width:141px;height:46px">Read More</a>
  <div class="ph about-photo" role="img" aria-label="Photo of a technician in a hard hat servicing an outdoor air conditioning unit"></div>
</section>

<!-- SERVICES -->
<section class="services">
  <p class="abs" style="left:0;width:1200px;text-align:center;top:77px;color:#fff;font-family:'Oswald',sans-serif;font-size:16px">WHAT WE DO</p>
  <h2 class="heading abs" style="left:0;width:1200px;text-align:center;top:100px;color:#fff;font-size:36px;font-weight:400">Our Services</h2>
  <article class="svc-card" style="left:79px">
    <div class="ph svc-img" style="background:linear-gradient(160deg,#e5e7ea,#b9c3cf 50%,#2e5fa6)" role="img" aria-label="Photo of a technician servicing a wall mounted air conditioner"></div>
    <h3>HVAC Maintenance &amp; Tune-Ups</h3>
    <p>Lorem ipsum dolor sit amet, consectetur adipiscing elit, sed do eiusmod tempor incididunt ut labore et dolore magna aliqua. Ut enim ad minim veniam, quis</p>
    <a class="btn" style="left:222px;top:192px;width:141px;height:44px">Read More</a>
  </article>
  <article class="svc-card" style="left:620px">
    <div class="ph svc-img" style="background:linear-gradient(160deg,#f2f3f4,#d6dbe0 50%,#8a3b2a)" role="img" aria-label="Photo of hands repairing a boiler with a pressure gauge"></div>
    <h3>Emergency HVAC Repairs</h3>
    <p>Lorem ipsum dolor sit amet, consectetur adipiscing elit, sed do eiusmod tempor incididunt ut labore et dolore magna aliqua. Ut enim ad minim veniam, quis</p>
    <a class="btn" style="left:222px;top:192px;width:141px;height:44px">Read More</a>
  </article>
</section>

<!-- SPECIALISE -->
<section>
  <p class="abs" style="left:0;width:1200px;text-align:center;top:2302px;font-family:'Oswald',sans-serif;font-size:16px;color:var(--ink)">WHY WE ARE</p>
  <h2 class="heading abs" style="left:0;width:1200px;text-align:center;top:2325px;font-size:36px;font-weight:400">Specialise Services</h2>
  <svg class="abs" style="left:100px;top:2410px" width="460" height="440" viewBox="0 0 460 440">
    <circle cx="210" cy="215" r="200" fill="none" stroke="#d7dde5" stroke-width="1.5"/>
    <circle cx="220" cy="210" r="178" fill="#0677BA"/>
    <circle cx="403" cy="130" r="6" fill="#F08F49"/>
    <circle cx="415" cy="210" r="6" fill="#F08F49"/>
    <circle cx="423" cy="306" r="6" fill="#F08F49"/>
    <circle cx="387" cy="380" r="6" fill="#F08F49"/>
  </svg>
  <div class="ph" style="left:130px;top:2460px;width:360px;height:300px;border-radius:50%;background:radial-gradient(circle at 55% 45%,rgba(245,188,146,.5),rgba(6,119,186,0) 65%)" role="img" aria-label="Illustration of flames over a photo of a technician"></div>
  <div class="ph" style="left:183px;top:2735px;width:298px;height:183px;border-radius:28px 14px 22px 22px;background:linear-gradient(160deg,#3b3f44,#15181b 60%,#2c3035)" role="img" aria-label="Photo of a black company service van"></div>

  <div class="spec-icon" style="left:483px;top:2421px"><svg width="32" height="32" viewBox="0 0 32 32" fill="none" stroke="#0677BA" stroke-width="1.6"><rect x="4" y="8" width="24" height="12" rx="2"/><path d="M8 14h16M8 24v4M16 24v4M24 24v4"/></svg></div>
  <div class="spec-item abs" style="left:572px;top:2420px;width:470px"><h4>HVAC Repair</h4><p>Lorem ipsum dolor sit amet, consectetur adipiscing elit, sed do eiusmod tempor incididunt ut labore et dolore magna aliqua.</p></div>

  <div class="spec-icon" style="left:550px;top:2527px"><svg width="32" height="32" viewBox="0 0 32 32" fill="none" stroke="#0677BA" stroke-width="1.6"><path d="M4 14 16 5l12 9"/><rect x="7" y="14" width="18" height="13"/><path d="M7 19h18M7 23h18M13 14v13M19 14v13"/></svg></div>
  <div class="spec-item abs" style="left:638px;top:2528px;width:460px"><h4>Geothermal</h4><p>Lorem ipsum dolor sit amet, consectetur adipiscing elit, sed do eiusmod tempor incididunt ut labore et dolore magna aliqua.</p></div>

  <div class="spec-icon" style="left:560px;top:2631px"><svg width="32" height="32" viewBox="0 0 32 32" fill="none" stroke="#0677BA" stroke-width="1.6"><rect x="5" y="6" width="16" height="21"/><path d="M9 11h3M14 11h3M9 16h3M14 16h3M9 21h3M14 21h3M21 14h6v13h-6"/></svg></div>
  <div class="spec-item abs" style="left:643px;top:2639px;width:460px"><h4>Commercial Repairs</h4><p>Lorem ipsum dolor sit amet, consectetur adipiscing elit, sed do eiusmod tempor incididunt ut labore et dolore magna aliqua.</p></div>

  <div class="spec-icon" style="left:522px;top:2738px"><svg width="32" height="32" viewBox="0 0 32 32" fill="none" stroke="#0677BA" stroke-width="1.6"><path d="M6 26 18 14M20 6a5 5 0 0 0 6 6l-3 3-6-6zM6 6l20 20M6 6l4 1 1 4"/></svg></div>
  <div class="spec-item abs" style="left:609px;top:2749px;width:460px"><h4>Maintenance &amp; Install</h4><p>Lorem ipsum dolor sit amet, consectetur adipiscing elit, sed do eiusmod tempor incididunt ut labore et dolore magna aliqua.</p></div>
</section>

<!-- ENERGY -->
<section class="energy">
  <h2 class="heading abs" style="left:88px;top:80px;color:#fff;font-size:37px;font-weight:400">Go the Energy Efficient Route</h2>
  <p class="abs" style="left:88px;top:139px;width:570px;color:#fff;font-size:13px;line-height:19.5px">Northpoint Air Conditioning, LLC provides a wide variety of residential and commercial HVAC services in the Brookfield, OK area. With over a decade of experience, our HVAC company to install, repair and maintain the HVAC systems in your home or commer cial building. Our technician can find out what's wrong with your mal functioning heating or cooling system and repair or replace it on the spot. We specialize in energy-efficient geothermal heating</p>
  <a class="btn" style="left:88px;top:279px;width:141px;height:44px">Learn More</a>
</section>
<div class="ph energy-photo" role="img" aria-label="Photo of a technician in overalls working on an indoor unit"></div>

<!-- REVIEWS -->
<section>
  <h2 class="heading abs" style="left:0;width:1200px;text-align:center;top:3585px;font-size:37px;font-weight:400">What Our Customers Say</h2>

  <article class="review" style="left:87px">
    <div class="quote"><svg width="46" height="38" viewBox="0 0 46 38"><path fill="#0054AA" d="M0 38V20C0 8 6 1 18 0v7c-6 1-9 5-9 11h9v20zm26 0V20C26 8 32 1 44 0v7c-6 1-9 5-9 11h9v20z"/></svg></div>
    <div class="stars"><span></span><span></span><span></span><span></span><span></span></div>
    <div class="verified"><svg width="13" height="13" viewBox="0 0 14 14"><circle cx="7" cy="7" r="7" fill="#8a8f96"/><path d="m4 7 2 2 4-4" stroke="#fff" stroke-width="1.6" fill="none"/></svg>Verified</div>
    <p>I've included a structured and detailed "Customer Reviews" section while keeping everything clean and modern. Let me know if you want any modifications or additional details!</p>
    <div class="who" style="top:182px">-Marisa</div>
  </article>

  <article class="review" style="left:441px">
    <div class="quote"><svg width="46" height="38" viewBox="0 0 46 38"><path fill="#0054AA" d="M0 38V20C0 8 6 1 18 0v7c-6 1-9 5-9 11h9v20zm26 0V20C26 8 32 1 44 0v7c-6 1-9 5-9 11h9v20z"/></svg></div>
    <div class="stars"><span></span><span></span><span></span><span></span><span></span></div>
    <div class="verified"><svg width="13" height="13" viewBox="0 0 14 14"><circle cx="7" cy="7" r="7" fill="#8a8f96"/><path d="m4 7 2 2 4-4" stroke="#fff" stroke-width="1.6" fill="none"/></svg>Verified</div>
    <p>I've included a structured and detailed "Customer Reviews" section while keeping everything clean and modern. Let me know if you want any modifications or additional details!</p>
    <div class="who" style="top:198px">-Danielle</div>
  </article>

  <article class="review" style="left:795px">
    <div class="quote"><svg width="46" height="38" viewBox="0 0 46 38"><path fill="#0054AA" d="M0 38V20C0 8 6 1 18 0v7c-6 1-9 5-9 11h9v20zm26 0V20C26 8 32 1 44 0v7c-6 1-9 5-9 11h9v20z"/></svg></div>
    <div class="stars"><span></span><span></span><span></span><span></span><span></span></div>
    <div class="verified"><svg width="13" height="13" viewBox="0 0 14 14"><circle cx="7" cy="7" r="7" fill="#8a8f96"/><path d="m4 7 2 2 4-4" stroke="#fff" stroke-width="1.6" fill="none"/></svg>Verified</div>
    <p>I've included a structured and detailed "Customer Reviews" section while keeping everything clean and modern. Let me know if you want any modifications or additional details!</p>
    <div class="who" style="top:182px">-Everett</div>
  </article>

  <svg class="abs" style="left:595px;top:4015px" width="66" height="12" viewBox="0 0 66 12">
    <circle cx="6" cy="6" r="4" fill="#7BADD7"/><circle cx="23" cy="6" r="4.5" fill="none" stroke="#7BADD7" stroke-width="1.5"/><circle cx="40" cy="6" r="4" fill="#7BADD7"/><circle cx="57" cy="6" r="4" fill="#7BADD7"/>
  </svg>
</section>

<!-- CONTACT -->
<section class="contact">
  <h2 class="heading abs" style="left:605px;top:80px;color:#fff;font-size:37px;font-weight:400">Get in Touch</h2>
  <div class="cfield" style="left:609px;top:149px;width:215px;height:40px">First Name*</div>
  <div class="cfield" style="left:834px;top:149px;width:218px;height:40px">Last Name*</div>
  <div class="cfield" style="left:609px;top:202px;width:215px;height:40px">Email address*</div>
  <div class="cfield" style="left:834px;top:202px;width:218px;height:40px">Phone Number*</div>
  <div class="cfield" style="left:609px;top:256px;width:443px;height:85px">Message*</div>
  <a class="btn" style="left:609px;top:366px;width:161px;height:43px">Submit Request</a>
  <div class="abs" style="left:824px;top:377px;color:#fff;font-size:13px;font-weight:600;display:flex;align-items:center;gap:8px">
    <svg width="22" height="22" viewBox="0 0 22 22"><circle cx="11" cy="11" r="11" fill="#fff"/><path fill="#0054AA" d="M8 9.5a8 8 0 0 0 4.5 4.5l1.2-1.2c.2-.2.4-.2.6-.1l1.8.6c.3.1.4.3.4.5V15c0 .4-.3.6-.6.6A9 9 0 0 1 6.4 6.6c0-.3.2-.6.6-.6h1.7c.3 0 .5.2.5.4l.6 1.8c.1.2 0 .4-.1.6z"/></svg>
    Call : + 555.014.2288
  </div>
</section>
<div class="ph contact-photo" role="img" aria-label="Photo of a technician in a blue cap and uniform with a tool belt"></div>

<!-- FOOTER -->
<footer class="footer">
  <div class="abs" style="left:150px;top:66px;width:170px;text-align:center">
    <div style="width:14px;height:14px;border-radius:50%;background:var(--orange);margin:0 auto 10px"></div>
    <div style="font-weight:700;font-size:16px;letter-spacing:3px;color:var(--blue)">STEADWELL</div>
    <div style="font-size:7.5px;letter-spacing:3px;color:var(--blue);font-weight:600;margin-top:2px">HEATING AND AIR</div>
  </div>
  <div class="abs" style="left:176px;top:231px"><span class="fsoc"></span><span class="fsoc"></span><span class="fsoc"></span><span class="fsoc"></span></div>

  <h5 style="left:410px;top:110px">Quick Links</h5>
  <ul style="left:416px;top:136px"><li>Home</li><li>ABOUT US</li><li>SERVICES</li><li>TESTIMONIALS</li><li>SPECIALS</li><li>CONTACT US</li></ul>

  <h5 style="left:614px;top:110px">Contact Us</h5>
  <ul style="left:620px;top:138px;line-height:15px">
    <li style="display:flex;gap:9px;align-items:center"><svg width="10" height="10" viewBox="0 0 24 24"><path fill="#fff" d="M6.6 10.8a15 15 0 0 0 6.6 6.6l2.2-2.2c.3-.3.7-.4 1-.2 1.1.4 2.3.6 3.6.6.6 0 1 .4 1 1V20c0 .6-.4 1-1 1A17 17 0 0 1 3 4c0-.6.4-1 1-1h3.5c.6 0 1 .4 1 1 0 1.3.2 2.5.6 3.6.1.3 0 .7-.2 1z"/></svg>555.014.2288</li>
    <li style="display:flex;gap:9px;align-items:center;margin-top:18px"><svg width="10" height="8" viewBox="0 0 20 16"><rect width="20" height="16" rx="2" fill="#fff"/><path d="m1 2 9 7 9-7" stroke="#0c1624" stroke-width="2" fill="none"/></svg><u>hello@steadwellmail.com</u></li>
    <li style="display:flex;gap:9px;margin-top:20px"><svg width="10" height="13" viewBox="0 0 16 22"><path fill="#fff" d="M8 0a8 8 0 0 0-8 8c0 6 8 14 8 14s8-8 8-14a8 8 0 0 0-8-8zm0 11a3 3 0 1 1 0-6 3 3 0 0 1 0 6z"/></svg><span>240 W. Linden Ave,<br>Fairview City, MO 64000</span></li>
  </ul>

  <h5 style="left:845px;top:110px">Subscribe Newsletter</h5>
  <p class="abs" style="left:855px;top:138px;width:210px;font-size:9.5px;line-height:14px">Subscribe newsletter for the latest offers and news</p>
  <div class="abs" style="left:845px;top:181px;width:168px;height:36px;background:#fff;border-radius:18px 0 0 18px;font-size:8.5px;color:#9aa3ad;padding:13px 20px">Enter Email...</div>
  <div class="abs" style="left:1013px;top:181px;width:44px;height:36px;background:var(--blue);border-radius:0 18px 18px 0;display:flex;align-items:center;justify-content:center"><svg width="16" height="10" viewBox="0 0 16 10"><path d="M0 5h14M10 1l4 4-4 4" stroke="#fff" stroke-width="1.6" fill="none"/></svg></div>

  <p class="abs" style="left:156px;top:317px;font-size:8.5px">Copyrights 2025, All Rights Reserved</p>
  <p class="abs" style="right:145px;top:317px;font-size:8.5px">Privacy Policy | Terms &amp; Conditions</p>
</footer>

</body>
</html>
```